Business Card Design For Office Furniture Clearance Company

Kestrel Office Clearance - our company name pretty much explains what we do, we clear offices for high end clients, mainly plc's and large international companies.

We require a nice looking business card that displays professionalism but without being too serious.

It would be nice to see just a little more than a conventional boring business card, make sure you add some flare.

Industry/Entity Type

Office Furniture

Contact Information for Business Card

CARD 1

Tom Pardew
Director
tom@kestrelofficeclearance.co.uk
m: 07700 513928

t: 01632 419063
www.kestrelofficeclearance.co.uk

Kestrel Office Clearance
Unit K4 B
3-7 Ferndale Lane
Ashcombe
Harlow Vale
ZZ9 4QX

free office clearances… you cant get better than that.

CARD 2

Henry Walbrook
Director
henry@kestrelofficeclearance.co.uk
m: 07700 628157

t: 01632 419063

Kestrel Office Clearance
Unit K4 B
3-7 Ferndale Lane
Ashcombe
Harlow Vale
ZZ9 4QX

Font styles to use
Sans Serif

Requirements
Must have
• A white background - as we have a blue logo.
Nice to have
• Nice use of the logo - play around with this and dissect it.

```html
<!DOCTYPE html>
<html lang="en">
<head>
<meta charset="utf-8">
<title>Kestrel Office Clearance – Business Card</title>
<link rel="stylesheet" href="https://fonts.googleapis.com/css2?family=Open+Sans:wght@400;600&display=swap">
<style>
  :root {
    --page-bg: #e6ebf1;
    --card-light: #f7f9fb;
    --card-dark: #1d4a80;
    --card-dark-deep: #163d6c;
    --brand-blue: #3a78b5;
    --badge-blue: #1f5597;
    --badge-ring: #e9eff6;
    --ink: #333a40;
    --on-dark: #f2f5f9;
    --icon-pill: #173f70;
  }
  * { margin: 0; padding: 0; box-sizing: border-box; }
  html, body {
    width: 1200px; height: 900px; overflow: hidden;
    background: var(--page-bg);
    font-family: "Open Sans", Arial, sans-serif;
  }
  .business-card {
    position: absolute; left: 225px; top: 236px;
    width: 750px; height: 427px;
    background: var(--card-light);
    box-shadow: 0 10px 30px rgba(20, 40, 70, 0.18);
    overflow: hidden;
  }
  .contact-panel {
    position: absolute; left: 376px; top: 0;
    width: 374px; height: 100%;
    background: linear-gradient(160deg, var(--card-dark) 0%, var(--card-dark-deep) 100%);
  }
  .brand-badge {
    position: absolute; left: 265px; top: 100px;
    width: 224px; height: 224px;
  }
  .holder-name {
    position: absolute; left: 26px; top: 114px;
    font-size: 26px; font-weight: 600; color: var(--brand-blue);
    letter-spacing: 0.2px;
  }
  .holder-role {
    position: absolute; left: 26px; top: 156px;
    font-size: 18px; color: var(--ink);
  }
  .company-name {
    position: absolute; left: 26px; top: 236px;
    font-size: 17px; font-weight: 600; color: var(--brand-blue);
  }
  .address-line {
    position: absolute; left: 26px;
    font-size: 17px; color: var(--ink);
  }
  .address-line.line-one { top: 270px; }
  .address-line.line-two { top: 304px; }
  .contact-item {
    position: absolute;
    font-size: 16px; color: var(--on-dark);
    line-height: 22px;
  }
  .contact-item.email { left: 475px; top: 135px; }
  .contact-item.mobile { left: 489px; top: 168px; }
  .contact-item.landline { left: 489px; top: 235px; }
  .contact-item.website { left: 475px; top: 268px; }
</style>
</head>
<body>
  <div class="business-card">
    <div class="contact-panel"></div>

    <svg class="brand-badge" viewBox="0 0 224 224" aria-hidden="true">
      <circle cx="112" cy="112" r="110" fill="var(--badge-ring)" opacity="0.9"/>
      <circle cx="112" cy="112" r="105" fill="var(--badge-blue)"/>
      <text x="96" y="120" text-anchor="middle" font-family="Open Sans, Arial, sans-serif"
            font-size="26" font-weight="600" fill="var(--on-dark)">Kestrel</text>
      <!-- email icon -->
      <rect x="150" y="39" width="40" height="22" rx="11" fill="var(--icon-pill)"/>
      <rect x="154" y="44" width="14" height="10" fill="#ffffff"/>
      <path d="M154 44 L161 50 L168 44" fill="none" stroke="var(--icon-pill)" stroke-width="1.2"/>
      <!-- mobile icon -->
      <rect x="178" y="72" width="40" height="22" rx="11" fill="var(--icon-pill)"/>
      <rect x="183" y="75" width="8" height="15" rx="1.5" fill="none" stroke="#ffffff" stroke-width="1.5"/>
      <!-- phone icon -->
      <rect x="178" y="138" width="40" height="22" rx="11" fill="var(--icon-pill)"/>
      <path d="M184 142 q-2 2 0 6 q3 5 8 7 q3 1 5 -1 l-3 -3 l-2 1 q-3 -1 -5 -5 l1 -2 z" fill="#ffffff"/>
      <!-- globe icon -->
      <rect x="150" y="172" width="40" height="22" rx="11" fill="var(--icon-pill)"/>
      <circle cx="161" cy="183" r="7" fill="none" stroke="#ffffff" stroke-width="1.3"/>
      <ellipse cx="161" cy="183" rx="3" ry="7" fill="none" stroke="#ffffff" stroke-width="1"/>
      <line x1="154" y1="183" x2="168" y2="183" stroke="#ffffff" stroke-width="1"/>
    </svg>

    <div class="holder-name">TOM PARDEW</div>
    <div class="holder-role">DIRECTOR</div>

    <div class="company-name">Kestrel Office Clearance</div>
    <div class="address-line line-one">Unit K4 B, 3-7 Ferndale Lane</div>
    <div class="address-line line-two">Ashcombe, Harlow Vale, ZZ9 4QX</div>

    <div class="contact-item email">tom@kestrelofficeclearance.co.uk</div>
    <div class="contact-item mobile">07700 513928</div>
    <div class="contact-item landline">01632 419063</div>
    <div class="contact-item website">www.kestrelofficeclearance.co.uk</div>
  </div>
</body>
</html>
```